trading data display webpage

We have build a rough wireframe of the two webpages that we want to display .The two wireframes are attached as a pdf document.
there will be login page. after login , the user will see the index page. that is the first page of the wireframe.

what we are displaying is essentially spread data. we are taking the difference in prices are two places and displaying the data. some calculations are done and is shown in the grid.

below the grid we show the behaviour on a graph. we will use bubble chart. I did not find a sample, hence have thrown in a placeholder.

this is time series data ( changes daily) and hence we need to check the behaviour.

the second wire frame shows how the user will choose the source price points and the destination price points.
we are talking here of natural gas prices hence the reference to source prices and destination prices.

you need to design the page/ pages such that the end-user loves it and is easy to use. the intent here is easy to use and easy to understand.
this will be responsive webpage since the end user will check it out on a tablet or a smartphone.

so if possible tell us how the navigation bar, the button bar, etc should fall when the screen size decreases.

I have uploaded 2 files. one is the wireframe ( pdf document) and second is the logo file.

please also let us know where to place the logo.

Target Market(s)

the target market is traders and data analyst

Industry/Entity Type

Build

Colors

Designer to choose colors to be used in the design.

Requirements
Must have
• 1. design for the web.
2. but think how the design will look when the screen size decreases.
3. tell if possible what screen components to keep and what to hide.

```html
<!DOCTYPE html>
<html lang="en">
<head>
<meta charset="utf-8">
<title>Natural Gas – Login</title>
<link rel="stylesheet" href="https://fonts.googleapis.com/css2?family=Figtree:wght@400;500;600;700&display=swap">
<style>
  :root {
    --page-bg: #e9edf2;
    --rule: #d6dbe0;
    --ink: #1b1d1f;
    --muted: #6b7882;
    --card-frame: #d9dde1;
    --card-bg: #ffffff;
    --card-head: #f4f7f9;
    --field-border: #c9cdd1;
    --field-focus: #8fb6de;
    --placeholder: #8e959b;
    --link: #0b55b5;
    --btn-top: #1a7ad9;
    --btn-bottom: #0756b3;
    --brand: #0b55b5;
  }
  * { box-sizing: border-box; margin: 0; padding: 0; }
  html, body {
    width: 1200px; height: 1200px; overflow: hidden;
    background: var(--page-bg);
    font-family: "Figtree", Arial, sans-serif;
    color: var(--ink);
  }
  .page { position: relative; width: 1200px; height: 1200px; }

  .top-nav { position: absolute; top: 30px; left: 870px; display: flex; align-items: center; gap: 22px; }
  .top-nav .help { font-size: 10px; color: var(--ink); text-decoration: none; }
  .top-nav .logout {
    display: inline-flex; align-items: center; justify-content: center;
    width: 60px; height: 23px; border: 1px solid #a9aeb3; border-radius: 12px;
    font-size: 12px; font-weight: 600; color: var(--ink); background: #f7f8fa;
  }

  .intro {
    position: absolute; left: 385px; top: 220px; width: 374px; height: 84px;
    border-top: 1px solid var(--rule); border-bottom: 1px solid var(--rule);
    text-align: center;
  }
  .intro h1 { font-size: 19px; font-weight: 400; margin-top: 17px; letter-spacing: 0.2px; }
  .intro p { font-size: 19px; font-weight: 400; margin-top: 10px; }

  .login-card {
    position: absolute; left: 389px; top: 329px; width: 371px; height: 418px;
    border: 4px solid var(--card-frame); border-radius: 4px; background: var(--card-bg);
  }
  .login-card .head {
    height: 45px; display: flex; background: linear-gradient(#fbfcfd, var(--card-head));
    border-bottom: 1px solid #e3e7ea;
  }
  .login-card .head h2 { flex: 1; font-size: 16px; font-weight: 700; color: var(--muted); padding: 16px 0 0 18px; }
  .login-card .head .avatar { width: 63px; border-left: 1px solid #e3e7ea; display: flex; align-items: center; justify-content: center; }

  .brand { position: absolute; top: 78px; left: 0; right: 0; display: flex; justify-content: center; align-items: center; gap: 8px; }
  .brand span { font-size: 20px; font-weight: 700; color: var(--brand); }
  .brand i { width: 12px; height: 12px; border-radius: 50%; background: var(--brand); display: block; }

  .field {
    position: absolute; height: 34px; border: 1px solid var(--field-border);
    font-size: 12.5px; color: var(--placeholder); padding: 10px 9px 0;
    box-shadow: inset 0 1px 2px rgba(0,0,0,0.06); background: #fff;
  }
  .field.username { left: 64px; top: 168px; width: 221px; height: 35px; border: 2px solid var(--field-focus); }
  .field.password { left: 66px; top: 224px; width: 220px; }

  .btn-login {
    position: absolute; left: 68px; top: 276px; width: 222px; height: 36px; border-radius: 2px;
    background: linear-gradient(var(--btn-top), var(--btn-bottom));
    color: #fff; font-size: 15px; font-weight: 700; display: flex; align-items: center; justify-content: center;
  }
  .remember { position: absolute; left: 70px; top: 333px; display: flex; align-items: center; gap: 8px; font-size: 12.5px; color: #4a5258; }
  .remember .box { width: 12px; height: 12px; border: 1px solid #aab0b5; border-radius: 2px; background: #dfe3e6; display: flex; align-items: center; justify-content: center; }
  .forgot { position: absolute; left: 73px; top: 362px; font-size: 12.5px; color: var(--link); }

  .create { position: absolute; top: 762px; left: 0; width: 1150px; text-align: center; font-size: 12.5px; color: var(--link); }
</style>
</head>
<body>
<div class="page">
  <nav class="top-nav">
    <a class="help" href="#">Help &amp; Support</a>
    <span class="logout">Logout</span>
  </nav>

  <header class="intro">
    <h1>NATURAL GAS</h1>
    <p>Search, Investigate, Get Real Time Prices</p>
  </header>

  <section class="login-card">
    <div class="head">
      <h2>LOGIN</h2>
      <div class="avatar">
        <svg width="24" height="24" viewBox="0 0 24 24" aria-hidden="true">
          <circle cx="12" cy="12" r="11" fill="#eef1f3" stroke="#6f7c86" stroke-width="1.2"/>
          <circle cx="12" cy="9" r="4" fill="#6f7c86"/>
          <path d="M4.5 19.5c1.5-3.5 4.3-5 7.5-5s6 1.5 7.5 5" fill="#6f7c86"/>
        </svg>
      </div>
    </div>

    <div class="brand"><i></i><span>GasSpread</span></div>

    <div class="field username">Username</div>
    <div class="field password">Password</div>
    <div class="btn-login">LOGIN</div>

    <label class="remember">
      <span class="box">
        <svg width="9" height="9" viewBox="0 0 10 10" aria-hidden="true"><path d="M1.5 5.2l2.3 2.3 4.7-5" fill="none" stroke="#4b5560" stroke-width="1.6"/></svg>
      </span>
      Do not close session
    </label>
    <a class="forgot">Forgot password?</a>
  </section>

  <a class="create">Create an Account</a>
</div>
</body>
</html>
```